Clean, Throwback Album Art needed

I'm looking for album art for an Indie Rock EP titled "The Quiet Lantern". The artist name is "Martin Kowalczyk"

I'm looking for a design that's wistful and nostalgic, but not depressing. I'm more interested in creative patterns and color combinations than anything else. I've uploaded two examples of album art I really like.

Please no stock images.

In addition to the album art, I will also need two variants of a back cover created in a complementary style- one with a track listing and one with marketing copy (e.g. Free download available at ___ ). These back covers do not have to be incredibly detailed, but can't just be text overlaid on top of of the front cover.

Details for back cover (track names, credits, etc.) will be provided to whoever submits the winning front cover design.

Requirements
Should not have
• No stock images. I need to know that I fully own the copyright to whatever work is produced.

```html
<!DOCTYPE html>
<html lang="en">
<head>
<meta charset="utf-8">
<title>The Quiet Lantern — Martin Kowalczyk</title>
<link href="https://fonts.googleapis.com/css2?family=Rye&display=swap" rel="stylesheet">
<style>
  :root {
    --sand: #c8b99b;
    --sand-light: #ddd2bb;
    --sand-pale: #ebe4d4;
    --sand-dark: #a89878;
    --ink-white: #f8f6f1;
    --shadow: rgba(70, 60, 45, 0.55);
  }
  * { margin: 0; padding: 0; box-sizing: border-box; }
  html, body {
    width: 1200px;
    height: 1200px;
    overflow: hidden;
    background: var(--sand);
  }
  .album-cover {
    position: relative;
    width: 1200px;
    height: 1200px;
    overflow: hidden;
  }
  .texture-field {
    position: absolute;
    inset: 0;
    background:
      radial-gradient(ellipse 420px 260px at 180px 220px, var(--sand-pale) 0%, transparent 70%),
      radial-gradient(ellipse 380px 240px at 980px 140px, var(--sand-light) 0%, transparent 70%),
      radial-gradient(ellipse 500px 300px at 300px 980px, var(--sand-light) 0%, transparent 70%),
      radial-gradient(ellipse 460px 280px at 1020px 1040px, var(--sand-pale) 0%, transparent 70%),
      radial-gradient(ellipse 520px 220px at 760px 860px, var(--sand-dark) 0%, transparent 72%),
      linear-gradient(155deg, var(--sand-light) 0%, var(--sand) 45%, var(--sand-dark) 75%, var(--sand) 100%);
  }
  .title-block {
    position: absolute;
    left: 0;
    right: 0;
    top: 405px;
    text-align: center;
    font-family: "Rye", serif;
    color: var(--ink-white);
    text-transform: uppercase;
    text-shadow: 6px 7px 8px var(--shadow);
    line-height: 1;
  }
  .title-lead {
    display: block;
    font-size: 96px;
    letter-spacing: 4px;
  }
  .title-main {
    display: block;
    font-size: 184px;
    letter-spacing: 2px;
    margin-top: 6px;
  }
  .artist-name {
    display: block;
    font-size: 54px;
    letter-spacing: 1px;
    margin-top: 2px;
  }
</style>
</head>
<body>
  <main class="album-cover">
    <div class="texture-field" role="img" aria-label="Weathered beige and cream marbled plaster texture with scratches and swirling streaks"></div>
    <h1 class="title-block">
      <span class="title-lead">The Quiet</span>
      <span class="title-main">Lantern</span>
      <span class="artist-name">Martin Kowalczyk</span>
    </h1>
  </main>
</body>
</html>
```